Stationery Design Project

KT7 Staffing requires letterhead and business card designs for a company based in London. Just like the name, we're a management resourcing company, providing resources to third party companies. You can see www.kt7staffing-example.com for ideas on existing colour schemes and design concepts that have been implimented and agreed to. Ultimately the design should broadcast professionalism, safety and the concept of growth.

Target Market(s)

Financial institutes; friendly societies (All UK based)

Industry/Entity Type

Safety

Requirements
Must have
• Files produced should be print ready; and the text in them editable (eg address, name etc)

```html
<!DOCTYPE html>
<html lang="en">
<head>
<meta charset="utf-8">
<title>KT7 Staffing – Stationery</title>
<link rel="stylesheet" href="https://fonts.googleapis.com/css2?family=Source+Sans+3:wght@400;600;700&display=swap">
<style>
  :root {
    --teal: #3f8a93;
    --teal-dark: #4e8688;
    --sky: #8fbcd8;
    --rule: #4f9aa3;
    --ink: #1a1a1a;
    --paper: #ffffff;
    --card-light: #f5f7f9;
    --card-edge: #d5dee5;
    --page: #ffffff;
  }
  * { box-sizing: border-box; margin: 0; padding: 0; }
  html, body {
    width: 1200px; height: 800px; overflow: hidden;
    background: var(--page);
    font-family: "Source Sans 3", "Myriad Pro", Arial, sans-serif;
  }
  .canvas { position: relative; width: 1200px; height: 800px; }

  /* Letterhead */
  .letterhead {
    position: absolute; left: 102px; top: 126px; width: 428px; height: 552px;
    background: var(--paper); border: 1px solid #e4e4e4;
  }
  .letterhead__brand {
    position: absolute; left: 30px; top: 26px;
    display: flex; align-items: center; gap: 8px;
  }
  .brand-dot { width: 14px; height: 14px; border-radius: 50%; background: var(--sky); }
  .letterhead__name {
    font-size: 24px; font-weight: 700; color: var(--teal); letter-spacing: 0.2px;
  }
  .letterhead__address {
    position: absolute; right: 52px; top: 46px; text-align: right;
    font-size: 8.6px; line-height: 11.6px; color: var(--teal);
  }
  .letterhead__body {
    position: absolute; left: 48px; top: 90px; width: 328px;
    font-size: 8.6px; line-height: 11.7px; color: var(--ink);
  }
  .letterhead__body .salutation { margin-bottom: 12px; }
  .letterhead__body p.para { text-indent: 12px; text-align: justify; margin-bottom: 11.7px; }
  .signature-area {
    position: absolute; left: 154px; top: 334px; width: 124px; height: 72px;
    background: linear-gradient(180deg, #ffffff, #f1f1f1);
  }
  .signature-line {
    position: absolute; left: 154px; top: 408px; width: 124px; height: 1.5px; background: var(--ink);
  }
  .signatory {
    position: absolute; left: 154px; top: 417px; width: 124px; text-align: center;
    font-size: 8.6px; line-height: 12px; color: var(--ink);
  }
  .letterhead__rule {
    position: absolute; left: 35px; top: 492px; width: 357px; height: 4px; background: var(--rule);
  }
  .letterhead__footer {
    position: absolute; left: 0; top: 511px; width: 428px; text-align: center;
    font-size: 8.6px; line-height: 11.6px; color: var(--teal);
  }

  /* Business cards */
  .card {
    position: absolute; left: 633px; width: 474px; height: 290px;
    border-radius: 12px; overflow: hidden;
    background: radial-gradient(ellipse at 45% 45%, var(--card-light) 0%, #e8edf1 55%, var(--card-edge) 100%);
  }
  .card--front { top: 100px; }
  .card--back { top: 414px; }

  .card__brand {
    position: absolute; left: 0; top: 88px; width: 474px;
    display: flex; align-items: center; justify-content: center; gap: 14px;
  }
  .card__brand .brand-dot { width: 26px; height: 26px; }
  .card__name { font-size: 56px; font-weight: 700; color: var(--teal); line-height: 1; }
  .card__band { position: absolute; left: 0; top: 236px; width: 474px; height: 54px; }
  .card__tagline {
    position: absolute; left: 0; top: 252px; width: 474px; text-align: center;
    font-size: 21px; color: #ffffff; letter-spacing: 0.2px;
  }

  .card__mark {
    position: absolute; left: 18px; top: 118px; width: 140px;
    font-size: 28px; font-weight: 700; color: var(--teal); line-height: 1.05;
  }
  .card__divider {
    position: absolute; left: 163px; top: 44px; width: 3px; height: 202px; background: var(--sky);
  }
  .card__role { position: absolute; left: 185px; top: 54px; color: var(--teal); }
  .card__role .holder { font-size: 21px; font-weight: 700; line-height: 26px; }
  .card__role .title { font-size: 20px; font-weight: 400; line-height: 26px; }
  .contact {
    position: absolute; left: 170px; top: 130px;
    display: grid; grid-template-columns: 74px 14px auto;
    font-size: 16px; line-height: 19.5px; color: var(--sky);
  }
  .contact dt { text-align: right; }
  .contact dd { display: contents; }
  .contact .bar { width: 2px; height: 15px; background: var(--sky); margin: 3px 0 0 6px; }
  .contact .bar--tall { height: 34px; }
</style>
</head>
<body>
<main class="canvas">

  <section class="letterhead" aria-label="Letterhead">
    <header class="letterhead__brand">
      <span class="brand-dot"></span>
      <span class="letterhead__name">KT7 Staffing</span>
    </header>
    <address class="letterhead__address" style="font-style:normal">
      45 Harbour Lane<br>Sampleton NSW 4021
    </address>
    <div class="letterhead__body">
      <p class="salutation">Dear Customer,</p>
      <p class="para">Pellentesque habitant morbi tristique senectus et netus et malesuada fames ac turpis egestas. Vestibulum tortor quam, feugiat vitae, ultricies eget, tempor sit amet, ante. Donec eu libero sit amet quam egestas semper. Aenean ultricies mi vitae est. Mauris placerat eleifend leo. Quisque sit amet est et sapien ullamcorper pharetra. Vestibulum erat wisi, condimentum sed, commodo vitae, ornare sit amet, wisi. Aenean fermentum, elit eget tincidunt condimentum, eros ipsum rutrum orci, sagittis tempus lacus enim ac dui. Donec non enim in turpis pulvinar facilisis. Ut felis. Praesent dapibus, neque id cursus faucibus, tortor neque egestas augue, eu vulputate magna eros eu erat. Aliquam erat volutpat. Nam dui mi, tincidunt quis, accumsan porttitor, facilisis luctus, metus.</p>
      <p class="para">Pellentesque habitant morbi tristique senectus et netus et malesuada fames ac turpis egestas. Vestibulum tortor quam, feugiat vitae, ultricies eget, tempor sit amet, ante. Donec eu libero sit amet quam egestas semper. Aenean ultricies mi vitae est. Mauris placerat eleifend leo.</p>
    </div>
    <div class="signature-area" role="img" aria-label="Handwritten signature of the director"></div>
    <div class="signature-line"></div>
    <p class="signatory">Project Owner<br>Director</p>
    <div class="letterhead__rule"></div>
    <footer class="letterhead__footer">
      45 Harbour Lane Sampleton NSW 4021<br>01 987 654320 - 01 765 432109
    </footer>
  </section>

  <section class="card card--front" aria-label="Business card front">
    <div class="card__brand">
      <span class="brand-dot"></span>
      <span class="card__name">KT7 Staffing</span>
    </div>
    <svg class="card__band" viewBox="0 0 474 54" preserveAspectRatio="none" aria-hidden="true">
      <path d="M0 0 Q237 14 474 0 L474 54 L0 54 Z" fill="var(--teal-dark)"/>
    </svg>
    <p class="card__tagline">Business Management Consultancy</p>
  </section>

  <section class="card card--back" aria-label="Business card back">
    <p class="card__mark">KT7<br>Staffing</p>
    <div class="card__divider"></div>
    <div class="card__role">
      <p class="holder">Project Owner</p>
      <p class="title">Director</p>
    </div>
    <dl class="contact">
      <dt>Adress</dt><dd><span class="bar bar--tall"></span><span>45 Harbour Lane<br>Sampleton NSW 4021</span></dd>
      <dt>Mobile</dt><dd><span class="bar"></span><span>01 987 654320</span></dd>
      <dt>Landline</dt><dd><span class="bar"></span><span>01 765 432109</span></dd>
      <dt>Email</dt><dd><span class="bar"></span><span>hello@kt7staffing-example.com</span></dd>
      <dt>Web</dt><dd><span class="bar"></span><span>www.kt7staffing-example.com</span></dd>
    </dl>
  </section>

</main>
</body>
</html>
```